MAPLE KEYS PROPERTY MANAGEMENT INC. WEBSITE

Please make the website more family-friendly.

I want a website to help me build my property management business by adding listing properties and creating an online application. Im open to any other ideas.
I want a WordPress designer to code it.

Here is my current website. www.maplekeys.biz

IDEA: I like the website design https://www.bluffcoveheatingandair.com/

Thank you

Tom

```html
<!DOCTYPE html>
<html lang="en">
<head>
<meta charset="utf-8">
<title>Maple Keys Property Management</title>
<link href="https://fonts.googleapis.com/css2?family=Montserrat:wght@500;600;700&family=Roboto:wght@400;500;700&display=swap" rel="stylesheet">
<style>
:root{
  --red:#c0171c;
  --red-dark:#9a1015;
  --ink:#262626;
  --charcoal:#2b2b2b;
  --text:#555;
  --muted:#777;
  --light:#efefef;
  --white:#fff;
}
*{margin:0;padding:0;box-sizing:border-box}
html,body{width:1200px;height:4138px;overflow:hidden}
body{position:relative;font-family:'Roboto',sans-serif;color:var(--ink);background:var(--white)}
.abs{position:absolute}
.heading{font-family:'Montserrat',sans-serif;font-weight:600;color:var(--ink);text-align:center}
.rule{position:absolute;left:50%;width:38px;height:3px;background:var(--red);transform:translateX(-50%)}
.btn{position:absolute;display:flex;align-items:center;justify-content:center;gap:8px;font-family:'Montserrat',sans-serif;font-weight:700;font-size:13px;color:var(--white);background:var(--red);text-transform:uppercase}
.icon{fill:none;stroke:currentColor;stroke-width:2;stroke-linecap:round;stroke-linejoin:round}

/* header */
.topbar{left:0;top:0;width:1200px;height:48px}
.topbar-info{left:345px;top:0;height:48px;display:flex;align-items:center;color:var(--white);font-size:13px}
.topbar-info .dot{width:26px;height:26px;border-radius:50%;background:var(--red);display:flex;align-items:center;justify-content:center;margin-right:14px}
.topbar-info .sep{width:2px;height:20px;background:var(--white);margin:0 38px}
.topbar-phone{font-size:17px;font-weight:500}
.socials{left:864px;top:9px;display:flex;gap:8px}
.socials span{width:30px;height:30px;border-radius:50%;background:var(--red)}
.brand{left:96px;top:18px;width:180px;text-align:center;color:var(--red);font-family:'Montserrat',sans-serif;font-weight:600}
.brand-mark{width:44px;height:44px;background:var(--red);margin:0 auto 8px}
.brand-name{font-size:22px;letter-spacing:1px;line-height:1}
.brand-sub{font-size:7.5px;letter-spacing:.6px;margin-top:4px}
.nav{top:78px;left:328px;display:flex;font-size:15px;color:#444}
.nav a{position:absolute;white-space:nowrap;color:inherit;text-decoration:none}
.user{left:1062px;top:74px;width:25px;height:25px;color:var(--ink)}

/* hero */
.hero{left:0;top:127px;width:1200px;height:660px;background:linear-gradient(160deg,#6f7b86 0%,#a9b1b6 40%,#8a8f92 65%,#4a4c4f 100%)}
.hero-title{left:0;top:372px;width:1200px;text-align:center;font-family:'Montserrat',sans-serif;font-weight:700;font-size:70px;color:var(--white);letter-spacing:1px}
.hero-sub{left:0;top:459px;width:1200px;text-align:center;font-family:'Montserrat',sans-serif;font-weight:500;font-size:28px;color:var(--white)}
.dots{left:568px;top:716px;display:flex;gap:5px}
.dots span{width:10px;height:10px;border-radius:50%;background:var(--white)}
.dots span:first-child{background:var(--red)}

/* call & search band */
.band{left:0;top:787px;width:1200px;height:170px}
.call-label{left:0;top:866px;width:320px;text-align:center;color:var(--white);font-size:20px;letter-spacing:1px}
.call-number{left:0;top:894px;width:320px;text-align:center;color:var(--white);font-size:27px;font-weight:700}
.field{position:absolute;top:853px;height:47px;background:var(--white);font-size:12px;color:#999;padding:14px 15px}

/* about */
.about-title{left:0;top:1062px;width:1200px;font-size:32px;line-height:41px}
.about-photo{left:141px;top:1179px;width:433px;height:355px;background:linear-gradient(180deg,#9ec3e6 0%,#d8d2c6 50%,#6a8a4a 100%)}
.about-text{left:631px;top:1180px;width:457px;font-size:14.5px;line-height:25.7px;color:var(--muted);text-align:justify}
.about-text p{margin-bottom:6px}

/* cities */
.cities{left:0;top:1635px;width:1200px;height:344px;background:var(--light)}
.city{position:absolute;top:1717px;width:238px;height:175px;border:3px solid var(--white);box-shadow:0 2px 6px rgba(0,0,0,.25)}
.city-label{position:absolute;top:1911px;width:238px;text-align:center;font-weight:500;font-size:15px;color:#333}
.arrow{position:absolute;top:1803px;width:36px;height:36px;border:1.5px solid #333;border-radius:50%;display:flex;align-items:center;justify-content:center;color:#333}

/* featured */
.featured-bg{left:0;top:1979px;width:1200px;height:714px}
.featured-title{left:0;top:2100px;width:1200px;font-size:32px;color:var(--white)}
.card{position:absolute;top:2176px;width:313px;height:426px;background:var(--white);padding:8px;box-shadow:0 3px 10px rgba(0,0,0,.2)}
.card-photo{height:196px}
.card-body{padding:20px 19px 0}
.card-title{font-weight:500;font-size:14px;line-height:22px;height:44px;color:#222}
.card-addr{font-size:14px;color:var(--muted);margin-top:5px}
.card-meta{display:flex;gap:20px;margin-top:14px;font-size:13px;color:#333}
.card-meta span,.card-size{display:flex;align-items:center;gap:8px}
.card-meta svg,.card-size svg{color:var(--red);width:16px;height:16px}
.card-size{font-size:13px;color:#333;margin-top:12px}
.card-price{font-weight:700;font-size:15px;color:var(--red);margin-top:14px}

/* mortgage */
.mortgage-title{left:0;top:2800px;width:1200px;font-size:32px}
.rates{left:172px;top:2875px;width:811px;height:305px;background:var(--white);box-shadow:0 4px 18px rgba(0,0,0,.12)}
.rates-head{height:58px;background:#f7f7f7}
.rates-divider{left:387px;top:0;width:1px;height:305px;background:#ddd}
.rates-cell{position:absolute;font-size:14.5px;color:#444}
.rates-h{position:absolute;top:18px;font-family:'Montserrat',sans-serif;font-weight:600;font-size:20px;color:#333}

/* contact */
.contact{left:0;top:3257px;width:1200px;height:570px;background:linear-gradient(90deg,#f4f4f4 0%,#ececec 55%,#e2e2e2 100%)}
.contact-photo{left:756px;top:3300px;width:444px;height:527px;background:linear-gradient(180deg,#f3f1ee 0%,#c9b8a8 50%,#8b6f5a 100%)}
.contact-title{left:112px;top:3370px;font-family:'Montserrat',sans-serif;font-weight:600;font-size:27px}
.contact-note{left:112px;top:3414px;width:480px;font-size:13.5px;line-height:21px;color:#444}
.input{position:absolute;height:43px;background:var(--white);border:1px solid #ddd;font-size:12px;color:#777;padding:14px 14px;display:flex;justify-content:space-between}
.input svg{width:13px;height:13px;color:#666}

/* footer */
.footer{left:0;top:3827px;width:1200px;height:254px;background:var(--ink)}
.foot-brand{left:112px;top:3880px;width:233px;text-align:center;color:var(--white);font-family:'Montserrat',sans-serif;font-weight:600}
.foot-brand .brand-mark{background:var(--white);width:56px;height:56px;margin-bottom:14px}
.foot-brand .brand-name{font-size:32px}
.foot-brand .brand-sub{font-size:11px}
.foot-icon{position:absolute;width:44px;height:44px;border:1.5px solid var(--white);border-radius:50%;display:flex;align-items:center;justify-content:center;color:var(--white)}
.foot-icon svg{width:18px;height:18px}
.foot-info{position:absolute;color:var(--white);font-size:14px;line-height:22px}
.foot-info b{font-size:13px;font-weight:700}
.foot-info .big{font-size:16px;font-weight:700}
.foot-nav{position:absolute;top:4001px;color:var(--white);font-size:15px;white-space:nowrap}
.bottom{left:0;top:4081px;width:1200px;height:57px;background:var(--red-dark);color:var(--white);font-size:14px}
</style>
</head>
<body>

<svg width="0" height="0" style="position:absolute">
  <defs>
    <symbol id="i-phone" viewBox="0 0 24 24"><path d="M22 16.9v3a2 2 0 0 1-2.2 2 19.8 19.8 0 0 1-8.6-3.1 19.5 19.5 0 0 1-6-6A19.8 19.8 0 0 1 2.1 4.2 2 2 0 0 1 4.1 2h3a2 2 0 0 1 2 1.7c.1 1 .4 1.9.7 2.8a2 2 0 0 1-.5 2.1L8 9.8a16 16 0 0 0 6 6l1.3-1.3a2 2 0 0 1 2.1-.4c.9.3 1.8.6 2.8.7a2 2 0 0 1 1.7 2z"/></symbol>
    <symbol id="i-mail" viewBox="0 0 24 24"><rect x="3" y="5" width="18" height="14" rx="1"/><path d="M3 6l9 7 9-7"/></symbol>
    <symbol id="i-pin" viewBox="0 0 24 24"><path d="M12 22s7-7 7-12a7 7 0 0 0-14 0c0 5 7 12 7 12z"/><circle cx="12" cy="10" r="2.5"/></symbol>
    <symbol id="i-user" viewBox="0 0 24 24"><circle cx="12" cy="12" r="10"/><circle cx="12" cy="10" r="3.5"/><path d="M5.5 19a7 7 0 0 1 13 0"/></symbol>
    <symbol id="i-search" viewBox="0 0 24 24"><circle cx="11" cy="11" r="7"/><path d="M21 21l-5-5"/></symbol>
    <symbol id="i-bath" viewBox="0 0 24 24"><path d="M3 12h18v3a4 4 0 0 1-4 4H7a4 4 0 0 1-4-4zM6 12V5a2 2 0 0 1 4 0"/></symbol>
    <symbol id="i-bed" viewBox="0 0 24 24"><path d="M2 19V6M2 14h20v5M22 14v-3a3 3 0 0 0-3-3h-8v6M6 11h2"/></symbol>
    <symbol id="i-size" viewBox="0 0 24 24"><rect x="5" y="3" width="14" height="18"/><path d="M9 8h6M9 12h6"/></symbol>
    <symbol id="i-arrow" viewBox="0 0 24 24"><circle cx="12" cy="12" r="10"/><path d="M10 8l4 4-4 4"/></symbol>
    <symbol id="i-chat" viewBox="0 0 24 24"><path d="M21 12a8 8 0 0 1-12 7l-5 1 1-4a8 8 0 1 1 16-4z"/></symbol>
    <symbol id="i-briefcase" viewBox="0 0 24 24"><rect x="3" y="7" width="18" height="13" rx="2"/><path d="M9 7V4h6v3"/></symbol>
  </defs>
</svg>

<!-- Header -->
<header>
  <svg class="abs topbar" viewBox="0 0 1200 48"><path d="M281 0H1200V48H311Z" fill="var(--charcoal)"/></svg>
  <div class="abs topbar-info">
    <span class="dot"><svg class="icon" width="14" height="14" style="color:#fff"><use href="#i-mail"/></svg></span>
    <span>info@maplekeys.biz</span>
    <span class="sep"></span>
    <span class="dot"><svg class="icon" width="13" height="13" style="color:#fff"><use href="#i-phone"/></svg></span>
    <span class="topbar-phone">(916) 555-0147</span>
    <span class="sep"></span>
  </div>
  <div class="abs socials" aria-label="Social links"><span></span><span></span><span></span><span></span><span></span><span></span></div>

  <div class="abs brand">
    <div class="brand-mark"></div>
    <div class="brand-name">MAPLE KEYS</div>
    <div class="brand-sub">PROPERTY MANAGEMENT &amp; SERVICES</div>
  </div>

  <nav class="abs nav" style="left:0;top:78px">
    <a style="left:328px">Home</a>
    <a style="left:395px">Listings</a>
    <a style="left:474px">Owners Prospect</a>
    <a style="left:617px">Tenants</a>
    <a style="left:697px">About</a>
    <a style="left:763px">Community</a>
    <a style="left:867px">Mortgage Info</a>
    <a style="left:989px;font-size:14px">Contact</a>
  </nav>
  <svg class="abs icon user"><use href="#i-user"/></svg>
</header>

<!-- Hero -->
<section>
  <div class="abs hero" role="img" aria-label="Two people shaking hands over a small model house on a desk"></div>
  <h1 class="abs hero-title">CALL TODAY</h1>
  <p class="abs hero-sub">&amp; Get 1 Month Property Management Fee Off. $120 Value!!</p>
  <a class="btn" style="left:514px;top:527px;width:172px;height:46px;font-size:14px">GET STARTED
    <svg class="icon" width="15" height="15"><use href="#i-arrow"/></svg></a>
  <div class="abs dots"><span></span><span></span><span></span><span></span><span></span></div>
</section>

<!-- Call & search band -->
<section>
  <svg class="abs band" viewBox="0 0 1200 170">
    <rect width="1200" height="170" fill="var(--charcoal)"/>
    <rect width="1200" height="4" fill="var(--red)"/>
    <path d="M0 0H378L312 170H0Z" fill="var(--red)"/>
    <path d="M94 0L159 -55L224 0Z" fill="var(--red)"/>
    <circle cx="159" cy="34" r="30" fill="var(--charcoal)"/>
  </svg>
  <svg class="abs icon" style="left:150px;top:812px;width:18px;height:18px;color:#fff"><use href="#i-phone"/></svg>
  <div class="abs call-label">CALL NOW :</div>
  <div class="abs call-number">(916) 555-0147</div>
  <div class="field" style="left:411px;width:162px">Address</div>
  <div class="field" style="left:583px;width:162px">City</div>
  <div class="field" style="left:755px;width:162px">Zip</div>
  <a class="btn" style="left:925px;top:853px;width:162px;height:47px;font-size:12px">SEARCH
    <svg class="icon" width="13" height="13"><use href="#i-search"/></svg></a>
</section>

<!-- About -->
<section>
  <div class="rule" style="top:1044px"></div>
  <h2 class="abs heading about-title">PROPERTY MANAGEMENT ELK GROVE,&nbsp; SACRAMENTO<br>&amp; SURROUNDING AREAS</h2>
  <div class="abs about-photo" role="img" aria-label="Suburban two-story house with a red For Rent sign on the front lawn"></div>
  <div class="abs about-text">
    <p>Having the right property manager means having an agent who is committed to helping you and making being a home provider hassle free. I believe clear communication, work ethic, time management, staying focused and knowledge goes a long way in my business.</p>
    <p>This commitment level has helped us build a remarkable track record of delivering results and maintaining a long lasting business partnership with our clients.</p>
    <p>Additionally whether you are an experienced investor or a first time home seller or buyer, we can help you in finding the property of your dreams. We truly feel excited and gratified when helping individuals meet their real estate needs.</p>
  </div>
  <a class="btn" style="left:631px;top:1489px;width:146px;height:40px">LEARN MORE</a>
  <a class="btn" style="left:787px;top:1489px;width:144px;height:40px;background:var(--ink)">LOGIN</a>
</section>

<!-- Cities -->
<section>
  <div class="abs cities"></div>
  <span class="arrow" style="left:38px"><svg class="icon" width="16" height="16" viewBox="0 0 24 24"><path d="M15 5l-7 7 7 7"/></svg></span>
  <span class="arrow" style="left:1124px"><svg class="icon" width="16" height="16" viewBox="0 0 24 24"><path d="M9 5l7 7-7 7"/></svg></span>
  <div class="city" style="left:108px;background:linear-gradient(180deg,#4f8fd6,#9cc3e8 55%,#5d7a4c)" role="img" aria-label="Sacramento riverfront skyline"></div>
  <div class="city" style="left:355px;background:linear-gradient(180deg,#3d77bf,#c98c4e 55%,#6b5a3a)" role="img" aria-label="Carmichael church reflected in water"></div>
  <div class="city" style="left:604px;background:linear-gradient(180deg,#8fb5d8,#c8712f 45%,#4c6b3a)" role="img" aria-label="Fair Oaks bridge over the river"></div>
  <div class="city" style="left:851px;background:linear-gradient(180deg,#9aa9b7,#d9b36a 50%,#3f5536)" role="img" aria-label="Folsom arch bridge at sunset"></div>
  <div class="city-label" style="left:108px">Sacramento</div>
  <div class="city-label" style="left:355px">Carmichael</div>
  <div class="city-label" style="left:604px">Fair Oaks</div>
  <div class="city-label" style="left:851px">Folsom</div>
</section>

<!-- Featured listings -->
<section>
  <svg class="abs featured-bg" viewBox="0 0 1200 714" preserveAspectRatio="none">
    <defs><linearGradient id="redFade" x1="0" y1="0" x2="0" y2="1"><stop offset="0" stop-color="#c0171c"/><stop offset="1" stop-color="#a31217"/></linearGradient></defs>
    <path d="M0 146L600 0L1200 146V714H0Z" fill="url(#redFade)"/>
  </svg>
  <div class="rule" style="top:2083px;background:#fff"></div>
  <h2 class="abs heading featured-title">FEATURED LISTINGS</h2>

  <article class="card" style="left:111px">
    <div class="card-photo" style="background:linear-gradient(180deg,#8db8e0,#d9c9a8 55%,#a48a62)" role="img" aria-label="Single-story home with a large tree in the front yard"></div>
    <div class="card-body">
      <div class="card-title">Fantastic opportunity 2 Bdrm x 1 Bth ADU Unit!!</div>
      <div class="card-addr">3170 Larkspur Ave Oakland, CA 94621</div>
      <div class="card-meta"><span><svg class="icon"><use href="#i-bath"/></svg>Bedrooms: 2</span><span><svg class="icon"><use href="#i-bed"/></svg>Bathrooms: 1</span></div>
      <div class="card-size"><svg class="icon"><use href="#i-size"/></svg>Residential Size: 693 Sq.</div>
      <div class="card-price">$2,000.00</div>
    </div>
  </article>

  <article class="card" style="left:443px">
    <div class="card-photo" style="background:linear-gradient(180deg,#3f86d6,#6a8c52 55%,#8a8a80)" role="img" aria-label="Ranch-style apartment building behind green trees"></div>
    <div class="card-body">
      <div class="card-title">7415 Hollow Oak Ave #3</div>
      <div class="card-addr">Carmichael, CA 95608</div>
      <div class="card-meta"><span><svg class="icon"><use href="#i-bath"/></svg>Bedrooms: 2</span><span><svg class="icon"><use href="#i-bed"/></svg>Bathrooms: 1</span></div>
      <div class="card-size"><svg class="icon"><use href="#i-size"/></svg>Residential Size: 1,350 Sq. Ft..</div>
      <div class="card-price">$2,000.00</div>
    </div>
  </article>

  <article class="card" style="left:776px">
    <div class="card-photo" style="background:linear-gradient(180deg,#f2f2f2,#d8d8d8 60%,#b7a89a)" role="img" aria-label="Bright apartment kitchen with white cabinets"></div>
    <div class="card-body">
      <div class="card-title">Nice &amp; Clean 3 bd. x 1 bth. Apartment.</div>
      <div class="card-addr">1840 Cedar St. #4 Sacramento, CA 95818</div>
      <div class="card-meta"><span><svg class="icon"><use href="#i-bath"/></svg>Bedrooms: 3</span><span><svg class="icon"><use href="#i-bed"/></svg>Bathrooms: 1</span></div>
      <div class="card-size"><svg class="icon"><use href="#i-size"/></svg>Residential Size: 693 Sq.</div>
      <div class="card-price">$1,695.00</div>
    </div>
  </article>
</section>

<!-- Mortgage rates -->
<section>
  <div class="rule" style="top:2781px"></div>
  <h2 class="abs heading mortgage-title">MORTGAGE RATES</h2>
  <div class="abs rates">
    <div class="rates-head"></div>
    <div class="abs rates-divider"></div>
    <div class="rates-h" style="left:106px">National</div>
    <div class="rates-h" style="left:551px;top:14px">Average Rate*</div>
    <div class="rates-cell" style="left:106px;top:79px">30-Year FHA Rate</div><div class="rates-cell" style="left:551px;top:79px">7.07%</div>
    <div class="rates-cell" style="left:106px;top:132px">30-Year Fixed Rate</div><div class="rates-cell" style="left:551px;top:132px">5.88%</div>
    <div class="rates-cell" style="left:106px;top:183px">20-Year Fixed Rate</div><div class="rates-cell" style="left:551px;top:183px">7.19%</div>
    <div class="rates-cell" style="left:106px;top:236px">15-Year Fixed Rate</div><div class="rates-cell" style="left:551px;top:236px">6.61%</div>
  </div>
</section>

<!-- Contact -->
<section>
  <div class="abs contact"></div>
  <div class="abs contact-photo" role="img" aria-label="Happy family running into their new home through open front doors"></div>
  <div class="abs" style="left:112px;top:3362px;width:38px;height:3px;background:var(--red)"></div>
  <h2 class="abs contact-title">CONTACT US</h2>
  <p class="abs contact-note">Your privacy is important to me. Your information will not be shared, sold or exchanged with anyone else.</p>
  <div class="input" style="left:112px;top:3472px;width:254px">First Name<svg class="icon"><use href="#i-user"/></svg></div>
  <div class="input" style="left:385px;top:3472px;width:256px">Last Name<svg class="icon"><use href="#i-user"/></svg></div>
  <div class="input" style="left:112px;top:3533px;width:254px">Phone No<svg class="icon"><use href="#i-phone"/></svg></div>
  <div class="input" style="left:385px;top:3533px;width:256px">Services<svg class="icon" viewBox="0 0 24 24"><path d="M6 9l6 6 6-6"/></svg></div>
  <div class="input" style="left:112px;top:3594px;width:527px;height:95px;align-items:flex-start">Additional Comments or Preferences<svg class="icon"><use href="#i-chat"/></svg></div>
  <a class="btn" style="left:112px;top:3716px;width:142px;height:41px;font-size:12px">SUBMIT NOW
    <svg class="icon" width="13" height="13"><use href="#i-arrow"/></svg></a>
</section>

<!-- Footer -->
<footer>
  <div class="abs footer"></div>
  <div class="abs foot-brand">
    <div class="brand-mark"></div>
    <div class="brand-name">MAPLE KEYS</div>
    <div class="brand-sub">PROPERTY MANAGEMENT &amp; SERVICES</div>
  </div>

  <span class="foot-icon" style="left:378px;top:3882px"><svg class="icon"><use href="#i-pin"/></svg></span>
  <div class="foot-info" style="left:450px;top:3884px"><b>EMAIL US</b><br>4810 Riverbend Rd. #112<br>Sacramento , CA 95822</div>

  <span class="foot-icon" style="left:646px;top:3892px"><svg class="icon"><use href="#i-phone"/></svg></span>
  <div class="foot-info" style="left:716px;top:3890px"><b>CALL US</b><br><span class="big">(916) 555-0147</span></div>

  <span class="foot-icon" style="left:895px;top:3892px"><svg class="icon"><use href="#i-briefcase"/></svg></span>
  <div class="foot-info" style="left:965px;top:3890px"><b>CALL US</b><br><span class="big">(916) 555-0147</span></div>

  <nav>
    <span class="foot-nav" style="left:379px">Home</span>
    <span class="foot-nav" style="left:446px">Listings</span>
    <span class="foot-nav" style="left:525px">Owners Prospect</span>
    <span class="foot-nav" style="left:668px">Tenants</span>
    <span class="foot-nav" style="left:748px">About</span>
    <span class="foot-nav" style="left:814px">Community</span>
    <span class="foot-nav" style="left:919px">Mortgage Info</span>
    <span class="foot-nav" style="left:1041px;font-size:14px">Contact</span>
  </nav>

  <div class="abs bottom">
    <span class="abs" style="left:112px;top:19px">&copy; 2024 Maple Keys. All Rights Reserved</span>
    <span class="abs" style="left:982px;top:19px">BRK# 02046318</span>
    <span class="abs" style="left:1144px;top:17px;font-size:11px">C47</span>
  </div>
</footer>

</body>
</html>
```